Harbor Nest Lodging website, brand new company, that rents rooms out in houses to milleniuls

We have a site right now that is weak as heck! We could use some punching it up. So we want it to be fun and cool, with added items in for social media (just chirpnet now) and anything else you want to throw at us. We do have a “blog” in there dedicated to events (we throw a lot of them) so want to incorporate that. Also have an existing design for a hand out that we want to use as our launching pad for colors… you can deviate from it a bit though.

Target Market(s)

25-40 year olds transitioning to the city from other places in the country. Millennial are the min group

Industry/Entity Type

Real Estate

Coding

Coded - Design and coding required

Number of Pages Required

5+ page

Font styles to use
Sans Serif

Requirements
Must have
• Fun look, same pages as those uploaded, but not necessarily the look and feel of what we have already.
• Follow the content of our posted site www.HarborNestLodging.example
• FOOTER
• LOGO | SITEMAP | SOCIAL LINKS | MAIN CTA REMINDER | CONTACT INFO | COPYRIGHT INFO | TERMS AND CONDITIONS
Nice to have
• Use as many of my graphics as loaded, but feel free to use stock photos as well interlaced. Including both people in their 20’s, 30’s, 40’s, having a fun time or of nice houses, inside and out.

```html
<!DOCTYPE html>
<html lang="en">
<head>
<meta charset="utf-8">
<title>Harbor Nest Lodging – Contact</title>
<link href="https://fonts.googleapis.com/css2?family=Montserrat:wght@400;500;600;700&display=swap" rel="stylesheet">
<style>
:root{
  --nav-bg:#2a2a2a;
  --blue:#3d95e8;
  --ink:#222;
  --line:#cfcfcf;
  --band:#f3f4f6;
  --footer:#3a3a3a;
  --footer-tile:#555;
  --footer-text:#d6d6d6;
  --white:#fff;
}
*{box-sizing:border-box;margin:0;padding:0}
html,body{width:914px;height:1200px;overflow:hidden;background:var(--white)}
body{position:relative;font-family:'Montserrat',sans-serif;color:var(--ink)}
.abs{position:absolute}
.hero{left:0;top:0;width:914px;height:405px;background:linear-gradient(100deg,#6f6a5e 0%,#b9b1a3 30%,#8f8578 55%,#3e2c28 80%,#5a4a40 100%)}
.nav{left:0;top:0;width:914px;height:64px;background:rgba(30,30,30,.85)}
.brand{left:178px;top:22px;display:flex;align-items:center;gap:6px;color:#5b8fd0;font-size:11px;font-weight:600}
.brand i{width:10px;height:10px;background:#5b8fd0;display:block}
.menu{right:12px;top:0;display:flex;height:64px}
.menu a{color:var(--white);font-size:8.5px;font-weight:600;text-decoration:none;padding:0 12.5px;line-height:58px;position:relative}
.menu a.active:after{content:"";position:absolute;left:0;right:0;bottom:16px;height:2px;background:var(--blue)}
.hero-title{left:0;width:914px;top:182px;text-align:center;color:var(--white);font-size:24px;font-weight:700;text-shadow:0 1px 3px rgba(0,0,0,.5)}
.hero-sub{left:0;width:914px;top:214px;text-align:center;color:var(--white);font-size:16px;font-weight:600;text-shadow:0 1px 3px rgba(0,0,0,.5)}
.quick{top:260px;width:80px;text-align:center;color:var(--white);font-size:8px;font-weight:600}
.quick svg{display:block;margin:0 auto 2px}
.lead-card{left:86px;top:340px;width:736px;height:84px;background:var(--white);border:1px solid #e4e4e4;border-top:0}
.field{height:22px;border:1px solid var(--line);font-size:7.5px;color:#888;padding:0 8px;line-height:20px;background:var(--white)}
.btn{background:var(--blue);color:var(--white);font-size:8px;font-weight:600;text-align:center;border-radius:1px}
.tagline{left:0;width:914px;top:396px;text-align:center;font-size:10.5px;font-weight:500}
.section-title{left:0;width:914px;text-align:center;font-size:13.5px;font-weight:600}
.info{left:188px;top:486px;width:250px;font-size:8px;line-height:17.4px}
.info h2{font-size:14px;font-weight:700;line-height:18px;margin-bottom:4px}
.divider{left:459px;top:475px;width:2px;height:222px;background:#555}
.communities{left:0;top:740px;width:914px;height:358px;background:var(--band)}
.card{background:var(--white)}
.card h3{font-size:10.5px;font-weight:600;position:absolute}
.card p{font-size:7.5px;position:absolute}
.dots{left:444px;top:1052px;display:flex;gap:4px}
.dots i{width:7px;height:7px;border-radius:50%;background:#e8e8ea;display:block}
.footer{left:0;top:1098px;width:914px;height:102px;background:var(--footer)}
.foot-brand{left:40px;top:1110px;display:flex;align-items:center;gap:5px;color:var(--white);font-size:9px;font-weight:600}
.foot-brand i{width:8px;height:8px;background:var(--blue);display:block}
.sitemap{left:0;width:914px;top:1111px;display:flex;justify-content:center;gap:12px}
.sitemap a{color:var(--footer-text);font-size:7px;font-weight:500;text-decoration:none}
.foot-cta{left:784px;top:1106px;width:90px;height:17px;line-height:17px;font-size:7px}
.social{top:1132px;height:24px;background:var(--footer-tile);color:var(--white);font-size:9px;font-weight:600;text-align:center;line-height:24px}
.copy{left:0;width:914px;top:1163px;text-align:center;color:var(--white);font-size:8px;font-weight:600}
.copy span{color:var(--footer-text);font-weight:500}
.foot-contact{left:0;width:914px;top:1180px;text-align:center;color:var(--footer-text);font-size:7px}
</style>
</head>
<body>
<div class="abs hero" role="img" aria-label="Photo of a furnished bedroom with a sleigh bed, window and house plant"></div>
<header class="abs nav">
  <div class="abs brand"><i></i>Harbor Nest Lodging</div>
  <nav class="abs menu">
    <a>Welcome</a><a>Our Communities</a><a>Amenities</a><a>Fitting</a><a>Events</a><a>About Us</a><a class="active">Contact</a>
  </nav>
</header>

<h1 class="abs hero-title">Welcome</h1>
<p class="abs hero-sub">Find your perfect rental room today!</p>

<div class="abs quick" style="left:261px">
  <svg width="40" height="34" viewBox="0 0 40 34" fill="none" stroke="#fff" stroke-width="1.6"><rect x="2" y="5" width="36" height="27"/><line x1="4" y1="2" x2="36" y2="2"/><path d="M5 29l10-11 8 8 5-5 9 8"/><circle cx="26" cy="14" r="3"/></svg>Gallery</div>
<div class="abs quick" style="left:414px">
  <svg width="42" height="34" viewBox="0 0 42 34" fill="none" stroke="#fff" stroke-width="1.6"><path d="M3 16L16 3l13 13"/><path d="M7 13v19h18"/><rect x="13" y="22" width="6" height="10"/><circle cx="31" cy="18" r="6"/><line x1="35" y1="23" x2="40" y2="30"/></svg>Rooms</div>
<div class="abs quick" style="left:567px">
  <svg width="40" height="34" viewBox="0 0 40 34" fill="none" stroke="#fff" stroke-width="1.6"><rect x="5" y="2" width="30" height="24"/><path d="M1 30h38v2H1z"/><path d="M13 12a10 10 0 0 1 14 0M16 15a5 5 0 0 1 8 0"/><circle cx="20" cy="18" r="1.2" fill="#fff"/></svg>Amenities</div>

<section class="abs lead-card">
  <div class="abs field" style="left:16px;top:23px;width:168px">Enter your name</div>
  <div class="abs field" style="left:195px;top:23px;width:168px">Enter your email address</div>
  <div class="abs field" style="left:374px;top:23px;width:167px;color:#333">I'm looking for...<span style="float:right;font-size:6px">▼</span></div>
  <div class="abs btn" style="left:560px;top:23px;width:150px;height:22px;line-height:22px">Submit</div>
</section>
<p class="abs tagline">Professional built Communities</p>

<h2 class="abs section-title" style="top:446px">Contact Us</h2>
<address class="abs info" style="font-style:normal">
  <h2>Harbor Nest Lodging</h2>
  <div>Saving money is just a nice perk</div>
  <div><b>Mailing</b></div>
  <div>PO Box 4820</div>
  <div>Bayport, NC 28000</div>
  <div><b>Email</b></div>
  <div>info@HarborNestLodging.example</div>
  <div><b>Phone</b></div>
  <div>555-014-2692</div>
</address>
<div class="abs divider"></div>
<form class="abs" style="left:0;top:0">
  <div class="abs field" style="left:472px;top:486px;width:237px">Enter your name</div>
  <div class="abs field" style="left:472px;top:515px;width:237px">Enter your phone number</div>
  <div class="abs field" style="left:472px;top:543px;width:237px">Enter your email address</div>
  <div class="abs field" style="left:472px;top:571px;width:237px;height:87px;line-height:26px">How may we help you?</div>
  <div class="abs btn" style="left:483px;top:664px;width:214px;height:21px;line-height:21px">Submit</div>
</form>

<section class="abs communities"></section>
<h2 class="abs section-title" style="top:757px">Our Communities</h2>

<article class="abs card" style="left:41px;top:780px;width:258px;height:261px">
  <div class="abs" style="left:6px;top:6px;width:246px;height:154px;background:linear-gradient(180deg,#5a92d6 0%,#8fb6e0 35%,#5d7fa0 60%,#3e6a2e 100%)" role="img" aria-label="Photo of a blue two-storey house with garden"></div>
  <h3 style="left:6px;top:168px">Alder Court</h3>
  <p style="left:6px;top:187px">5 Bedroom | 4.5 Bath | 2,890 Sq. Ft</p>
  <p style="left:6px;top:205px">Westgate</p>
  <div class="abs btn" style="left:178px;top:226px;width:72px;height:22px;line-height:22px">$500 | Rent</div>
</article>
<article class="abs card" style="left:324px;top:780px;width:259px;height:262px;box-shadow:0 1px 4px rgba(0,0,0,.35)">
  <div class="abs" style="left:7px;top:6px;width:246px;height:185px;background:linear-gradient(180deg,#b9c9d6 0%,#e8e6df 40%,#6d7d4a 75%,#8a4a34 100%)" role="img" aria-label="Photo of a white two-storey house with front steps"></div>
  <h3 style="left:7px;top:198px">Maplewood Row</h3>
  <p style="left:7px;top:218px">6 Bedroom | 4 Bath | 2,690 Sq. Ft</p>
  <p style="left:7px;top:236px">Riverbend</p>
  <div class="abs btn" style="left:178px;top:226px;width:73px;height:22px;line-height:22px">$500 | Rent</div>
</article>
<article class="abs card" style="left:608px;top:780px;width:258px;height:261px">
  <div class="abs" style="left:6px;top:6px;width:247px;height:164px;background:linear-gradient(160deg,#c9b06a 0%,#6f7a3a 40%,#3e4a26 70%,#8a7a5a 100%)" role="img" aria-label="Photo of a backyard patio with outdoor fireplace and chairs"></div>
  <h3 style="left:6px;top:178px">Cedar Hollow</h3>
  <p style="left:6px;top:197px">7 Bedroom | 5 Bath | 3,890 Sq. Ft</p>
  <p style="left:6px;top:215px">Oakmere</p>
  <div class="abs btn" style="left:179px;top:226px;width:72px;height:22px;line-height:22px">$500 | Rent</div>
</article>
<div class="abs dots"><i></i><i></i></div>

<footer class="abs footer"></footer>
<div class="abs foot-brand"><i></i>Harbor Nest Lodging</div>
<nav class="abs sitemap">
  <a>Welcome</a><a>Our Communities</a><a>Amenities</a><a>Fitting</a><a>Events</a><a>About Us</a><a>Contact</a>
</nav>
<div class="abs btn foot-cta">Find your room</div>
<div class="abs social" style="left:190px;width:157px">friendlink</div>
<div class="abs social" style="left:375px;width:157px">chirpnet</div>
<div class="abs social" style="left:561px;width:156px">snapframe</div>
<p class="abs copy">Copyright © Harbor Nest Lodging <span>· Terms and Conditions</span></p>
<p class="abs foot-contact">PO Box 4820, Bayport, NC 28000 · info@HarborNestLodging.example · 555-014-2692</p>
</body>
</html>
```